Hurricane Damage Public Adjuster Billboard

I have created several projects with you and have several great designs. I need to format them into a Billboard for upcoming Hurricane Season. Need done in a month. Im also in process of getting an eye catching and easy to remember 800# Vanity phone number like Call 800-Stormfix or 800- Need Help? My included past Sketch Guild projects will give you an idea of what colors, schemes, and designs I gravitate towards. 3 past Design projects were 1) 2 Logos where I picked the 1st place and the 2nd place and 2) Index Card where I picked the winner as the Index Card and the 2nd place as a Post Card. Point is, I will pick and pay for 2 winners if they're good. This should help to sweeten the pot. Also, please look at my website for ideas that I like:

www.TheClaimWardenGroup.com
I want people to feel that I am the best and highest. Level.

I've been getting a lot of quick half effort designs basically cut & pasting my previous projects. Please don't rush and take your time to be creative. A an example, my Biggest Competitor is Crestline Public Adjusting. Their colors are Black and Gold while mine are Blue, White, and Black with a highlight of Orange if possible. I JUST imported a picture of their BillBoard. I need mine better and BLOW AWAY THEIRS. Terms like "Don't be Victimized Twice ?, Don't let the Hurricane Ruin your Life?". "Get Fairly Paid & Move On" "Our Clients Claims are VIP?
Updates

I'm getting a lot of quick half effort ones. I'd rather you take your time and really put some thoughts and effort into it. My Biggest Competitor is Crestline Public Adjusting. They have black & gold colors, while I have Blue, Black, and white.

It needs to blow theirs away. I have imported their Billboard for comparative purposes.

Guy's,
I'll make it easier for you in what I'm looking for. Please look at the Crestline Billboard picture attached.

1) Put my "Blue Shield" to the left, replacing their logo
2) change color patterns from their (Black, Gold, White) to my color schemes of (Black, Blue, White)
3) I want to see my name where their is:

THE
Claim Warden Group
EXPERT & LOCAL Public Adjusters
"FOR THE POLICYHOLDER!!"

4) to the right, add the A+Rated logo and QTR+ Accredited logo, 5 Star Zentrio Rated logo, 5 Start BLOCKLINK Highly Rated logo, etc..

5) the right side is where you can be creative as I will not have a picture of me there.

"20+ Years of Experience, Recovering Millions for our VIP Clients"

"Your Best, Locally-Based Private Adjuster & Advocate'
"FOR THE POLICYHOLDER!!"

"Don't be victimized Twice!!"

"Don't let the Hurricane Ruin Your Life!!"

This should really help. Also, refer to my website, maybe a couple testimonial fillers?

Thanks all,

marvin@TheClaimWardenGroup.com

Just imported a few awards that would look great to the right side with all the other 5 Star Ratings and accolades.
This right section could be titled like zmy Website:

5 Star Reviews, Ratings & Awards:
4-5 Logos underneath?

Target Market(s)

Coastal place where a Hurricane 🌀 🌀 Hits

Industry/Entity Type

Hurricane Public Insurance Adjuster

Font styles to use
Sans Serif
Other font styles liked:
• Calvera fonts

Colors
0054AA
0677BA
7BADD7
CADEEF
E8F1F8
EE7325
F08F49
F5BC92
FAE3D3
FDF4ED

Requirements
Must have
• Use my past project logos, colors, and schemes to create eye grabbing BillBoard
Nice to have
Should not have
• Not be too busy, must be Easy to Read, Eye Catchy

```html
<!DOCTYPE html>
<html lang="en">
<head>
<meta charset="utf-8">
<title>The Claim Warden Group – Hurricane Billboard</title>
<link rel="stylesheet" href="https://fonts.googleapis.com/css2?family=Cinzel:wght@600;700&family=Hind:wght@600;700&family=Poppins:wght@500;800;900&display=swap">
<style>
  :root {
    --page: #e9eef3;
    --navy: #1f2636;
    --navy-deep: #151a24;
    --horizon: #b8493a;
    --dusk: #5a3a4a;
    --ground: #3a3a2e;
    --white: #ffffff;
    --sky-blue: #1aa3d9;
    --brand-blue: #0a9ee0;
    --indigo: #2e2f8f;
    --alert-red: #ee1c25;
    --alert-orange: #ff8a00;
    --star: #f5a623;
    --photo-warm: #b08a62;
    --photo-dark: #4a3b34;
  }
  html, body {
    margin: 0;
    width: 1200px;
    height: 546px;
    overflow: hidden;
    background: var(--page);
  }
  .billboard {
    display: block;
    width: 1200px;
    height: 546px;
  }
  .brand-title { font-family: "Cinzel", serif; font-weight: 700; fill: var(--white); }
  .brand-subtitle { font-family: "Hind", sans-serif; font-weight: 700; fill: var(--white); }
  .brand-tag { font-family: "Hind", sans-serif; font-weight: 700; fill: var(--navy-deep); }
  .brand-mark-name { font-family: "Poppins", sans-serif; font-weight: 800; fill: var(--brand-blue); }
  .phone-number { font-family: "Poppins", sans-serif; font-weight: 800; fill: var(--white); }
  .website { font-family: "Poppins", sans-serif; font-weight: 500; fill: var(--white); }
  .slogan { font-family: "Poppins", sans-serif; font-weight: 900; }
  .slogan-red { fill: var(--alert-red); }
  .slogan-orange { fill: var(--alert-orange); }
  .rating-stars { fill: var(--star); }
</style>
</head>
<body>
<svg class="billboard" viewBox="0 0 1200 546" xmlns="http://www.w3.org/2000/svg">
  <defs>
    <linearGradient id="sky" x1="0" y1="0" x2="0" y2="1">
      <stop offset="0" stop-color="var(--navy)"/>
      <stop offset="0.45" stop-color="var(--dusk)"/>
      <stop offset="0.78" stop-color="var(--horizon)"/>
      <stop offset="1" stop-color="var(--navy-deep)"/>
    </linearGradient>
    <linearGradient id="phoneBand" x1="0" y1="0" x2="1" y2="0">
      <stop offset="0" stop-color="var(--sky-blue)"/>
      <stop offset="1" stop-color="var(--indigo)"/>
    </linearGradient>
    <linearGradient id="stormPhoto" x1="0" y1="0" x2="0" y2="1">
      <stop offset="0" stop-color="var(--photo-dark)"/>
      <stop offset="1" stop-color="var(--photo-warm)"/>
    </linearGradient>
  </defs>

  <g class="design" transform="translate(0 102)">
    <!-- storm sky backdrop -->
    <rect class="sky-backdrop" x="0" y="0" width="1200" height="341" fill="url(#sky)"/>
    <rect class="ground-strip" x="0" y="237" width="300" height="40" fill="var(--ground)"/>
    <rect class="bottom-shade" x="0" y="277" width="1200" height="64" fill="var(--navy-deep)"/>

    <!-- hurricane damage photo area -->
    <polygon class="storm-photo" role="img" aria-label="Photo of a hurricane-wrecked house on sand under a lightning storm"
             points="592,110 880,110 929,341 592,341" fill="url(#stormPhoto)" opacity="0.9"/>

    <!-- brand mark area -->
    <g class="brand-mark">
      <circle cx="161" cy="110" r="18" fill="var(--brand-blue)"/>
      <text class="brand-mark-name" x="161" y="166" font-size="26" text-anchor="middle">CLAIM</text>
      <text class="brand-mark-name" x="161" y="196" font-size="26" text-anchor="middle">WARDEN</text>
    </g>

    <!-- company name -->
    <text class="brand-title" x="491" y="105" font-size="38" text-anchor="middle" textLength="400" lengthAdjust="spacingAndGlyphs">THE CLAIM WARDEN</text>
    <line x1="313" y1="129" x2="392" y2="129" stroke="var(--white)" stroke-width="3"/>
    <line x1="590" y1="129" x2="669" y2="129" stroke="var(--white)" stroke-width="3"/>
    <text class="brand-title" x="491" y="140" font-size="34" font-weight="600" text-anchor="middle">GROUP</text>
    <text class="brand-subtitle" x="491" y="168" font-size="20" text-anchor="middle" textLength="344" lengthAdjust="spacingAndGlyphs">EXPERT &amp; LOCAL PUBLIC ADJUSTERS</text>
    <rect class="brand-tag-box" x="364" y="177" width="254" height="22" fill="var(--sky-blue)"/>
    <text class="brand-tag" x="491" y="195" font-size="19" text-anchor="middle" textLength="240" lengthAdjust="spacingAndGlyphs">FOR THE POLICYHOLDER!!</text>

    <!-- accreditation strip -->
    <polygon class="badge-strip-accent" points="244,230 256,230 287,291 275,291" fill="var(--sky-blue)"/>
    <polygon class="badge-strip" points="254,230 531,230 552,291 285,291" fill="var(--white)"/>
    <rect class="badge rating-badge" x="286" y="240" width="87" height="40" rx="4" fill="none" stroke="var(--alert-red)" stroke-width="2"/>
    <circle class="badge club-badge" cx="409" cy="260" r="21" fill="var(--star)"/>
    <rect class="badge accredited-badge" x="441" y="242" width="80" height="30" rx="4" fill="var(--brand-blue)"/>

    <!-- phone band -->
    <polygon class="phone-band" points="531,230 909,230 929,291 552,291" fill="url(#phoneBand)"/>
    <text class="phone-number" x="568" y="283" font-size="52" textLength="318" lengthAdjust="spacingAndGlyphs">850-555-0142</text>

    <text class="website" x="491" y="323" font-size="16" text-anchor="middle">www.TheClaimWardenGroup.com</text>

    <!-- slogan panel -->
    <polygon class="slogan-divider" points="829,0 840,0 940,341 929,341" fill="var(--white)"/>
    <polygon class="slogan-panel" points="836,0 1200,0 1200,341 937,341" fill="#000"/>
    <text class="slogan slogan-red" x="1048" y="90" font-size="68" text-anchor="middle" textLength="208" lengthAdjust="spacingAndGlyphs">DON'T</text>
    <text class="slogan slogan-orange" x="1048" y="131" font-size="40" text-anchor="middle" textLength="155" lengthAdjust="spacingAndGlyphs">LET THE</text>
    <text class="slogan slogan-red" x="1048" y="184" font-size="56" text-anchor="middle" textLength="259" lengthAdjust="spacingAndGlyphs">HURRICANE</text>
    <text class="slogan slogan-orange" x="1048" y="239" font-size="62" text-anchor="middle" textLength="155" lengthAdjust="spacingAndGlyphs">RUIN</text>
    <text class="slogan slogan-red" x="1048" y="277" font-size="37" text-anchor="middle" textLength="215" lengthAdjust="spacingAndGlyphs">YOUR LIFE!!</text>
    <g class="rating-stars">
      <polygon points="1006,290 1008,295 1013,295 1009,298 1011,303 1006,300 1001,303 1003,298 999,295 1004,295"/>
      <polygon points="1024,290 1026,295 1031,295 1027,298 1029,303 1024,300 1019,303 1021,298 1017,295 1022,295"/>
      <polygon points="1042,290 1044,295 1049,295 1045,298 1047,303 1042,300 1037,303 1039,298 1035,295 1040,295"/>
      <polygon points="1060,290 1062,295 1067,295 1063,298 1065,303 1060,300 1055,303 1057,298 1053,295 1058,295"/>
      <polygon points="1078,290 1080,295 1085,295 1081,298 1083,303 1078,300 1073,303 1075,298 1071,295 1076,295"/>
    </g>
  </g>
</svg>
</body>
</html>
```